Tamaru Peruvian Cuisine needs a take-out menu

We need a new tri-fold 8.5"x11" take out menu for a Peruvian restaurant based in New Rochelle, NY. We have a vast selections of dishes from appetizers, seafood based dishes, desserts, Peruvian ceviches and more. We have attached the following:

Restaurant information
Pictures of our dishes
Tamaru Logo in pdf format
Menu in word format
Old take out menu for reference only! (our dishes have changed)
Updates

Project Deadline Extended
Reason: Need more time to make final decision.

Industry/Entity Type

Restaurant

```html
<!DOCTYPE html>
<html lang="en">
<head>
<meta charset="utf-8">
<title>Tamaru Peruvian Cuisine – Take-Out Menu</title>
<link href="https://fonts.googleapis.com/css2?family=Cinzel:wght@400;700&family=Playfair+Display:ital,wght@1,400;1,700&family=Tinos:wght@400;700&family=Arimo:wght@400;700&display=swap" rel="stylesheet">
<style>
:root{
  --brown:#5b3a21;
  --cream:#f1ead4;
  --edge:#d8caa6;
  --green:#34a863;
  --green-light:#7fd06f;
  --ink:#1f1a14;
  --muted:#3d3328;
  --gold:#e2b23c;
  --white:#ffffff;
}
*{box-sizing:border-box;margin:0;padding:0}
html,body{width:766px;height:1200px;overflow:hidden;background:var(--white)}
.sheet{position:relative;width:766px;height:1200px}
.fold{position:absolute;left:0;width:766px;background:var(--brown)}
.fold--outside{top:0;height:588px}
.fold--inside{top:608px;height:592px}
.panel{position:absolute;background:var(--cream);border:3px solid var(--edge);border-radius:6px;padding:6px 9px;font-family:"Tinos",serif;color:var(--ink)}
.col{display:flex;flex-direction:column;justify-content:space-between}
.section-title{font-family:"Playfair Display",serif;font-style:italic;color:var(--green);font-size:14px;text-align:center;line-height:1.1;margin-bottom:3px}
.section-title small{font-size:11px;text-transform:uppercase}
.item{margin-bottom:4px}
.item-name{display:flex;align-items:baseline;font-weight:700;font-size:9.3px;line-height:1.15}
.leader{flex:1;border-bottom:1.2px dotted var(--ink);margin:0 1px 2px}
.variants{display:flex;gap:4px;font-weight:700;font-size:7.6px;line-height:1.2;padding-left:6px}
.variants span{display:flex;flex:1;align-items:baseline}
.desc{font-size:6.6px;line-height:1.15;color:var(--muted);padding-left:6px}
.photo-slot{position:relative}
.photo{position:absolute;border:3px solid var(--green);border-radius:50%;background:radial-gradient(circle at 45% 45%,#f4f1ea 0 35%,#d99a4c 60%,#8c5a2e 100%)}
.photo--seafood{background:radial-gradient(circle at 50% 50%,#f8f5ef 0 30%,#e6b9c4 55%,#b24a3a 100%)}
.photo--meat{background:radial-gradient(circle at 50% 50%,#f6eee0 0 30%,#a4552b 60%,#5e3218 100%)}
.photo--scene{position:absolute;border-radius:2px;background:linear-gradient(180deg,#9fb6c4 0%,#7d8b6a 45%,#4b5a36 100%)}
.photo-label{position:absolute;font-family:"Playfair Display",serif;font-style:italic;font-weight:700;font-size:8px;color:var(--green);line-height:1;white-space:nowrap}
.cover{position:absolute;left:498px;top:0;width:268px;height:588px;text-align:center;color:var(--white);font-family:"Arimo",sans-serif}
.cover-menu{position:absolute;left:40px;top:12px;font-family:"Playfair Display",serif;font-style:italic;font-weight:700;font-size:22px;color:#e9d7a8}
.brand{position:absolute;left:58px;top:142px;width:148px;height:72px;border-radius:50%;background:var(--cream);border:5px solid var(--green);display:flex;align-items:center;justify-content:center;font-family:"Tinos",serif;font-size:22px;color:var(--green)}
.cover-title{position:absolute;left:0;width:268px;font-family:"Cinzel",serif;color:#f3ead7}
.cover-line{position:absolute;left:0;width:268px}
</style>
</head>
<body>
<div class="sheet">

<section class="fold fold--outside">

  <div class="panel col" style="left:19px;top:20px;width:224px;height:552px;justify-content:flex-start">
    <h2 class="section-title">Para Picar / <small>Appetizers</small></h2>
    <div class="col" style="height:395px">
      <div><div class="item-name">Chicharron de Calamares<span class="leader"></span>$12.95</div><p class="desc">crispy fried calamari served with house tartar sauce and salsa criolla</p></div>
      <div><div class="item-name">Anticucho Carretillero<span class="leader"></span>$15.95</div><p class="desc">choice of chicken or cow's heart Peruvian style kebabs, served with Cusco corn and grilled potatoes Corazon</p></div>
      <div><div class="item-name">Palta Rellena <small style="font-size:7px">with-</small></div><div class="variants"><span>Camarones<span class="leader"></span>$11.95</span><span>Pollo<span class="leader"></span>$8.95</span></div><p class="desc">Peruvian avocado stuffed with choice of chicken or shrimp, marinated in Peruvian spices</p></div>
      <div><div class="item-name">Tamal Criollo<span class="leader"></span>$5.95</div><p class="desc">Peruvian chicken tamale, served with salsa criolla</p></div>
      <div><div class="item-name">Salchipapa<span class="leader"></span>$9.95</div><p class="desc">French fries mixed with sliced hot dogs</p></div>
      <div><div class="item-name">Papa a la Huancaina<span class="leader"></span>$8.95</div><p class="desc">boiled potatoes, topped with ají amarillo and queso fresco sauce, egg, olives</p></div>
      <div><div class="item-name">Ocopa Arequipeña<span class="leader"></span>$8.95</div><p class="desc">boiled potatoes, topped with huacatay and queso fresco sauce, egg, olives</p></div>
      <div><div class="item-name">Empanada Limeña<span class="leader"></span>$3.95</div><p class="desc">patties stuffed with choice of chicken or beef</p></div>
      <div><div class="item-name">Causa <small style="font-size:7px">with-</small></div><div class="variants"><span>Camarones<span class="leader"></span>$9.95</span><span>Pollo<span class="leader"></span>$7.95</span></div><p class="desc">cold mashed potato infused with key of lime juice, pressed into a cake with choice of chicken or shrimp</p></div>
      <div><div class="item-name">Choritos a la Chalaca<span class="leader"></span>$10.95</div><p class="desc">steamed mussels topped with diced onions, tomatoes, lime juice and Cusco corn</p></div>
      <div><div class="item-name">Piqueo Tamaru<span class="leader"></span>$19.95</div><p class="desc">dishes combined of Chicharron de Calamares, Papa a la Huancaina, Choritos a la Chalaca and Causa</p></div>
    </div>
  </div>
  <div class="photo photo--seafood" role="img" aria-label="Photo of stuffed avocado with shrimp" style="left:22px;top:456px;width:108px;height:68px"></div>
  <div class="photo" role="img" aria-label="Photo of crab empanada with dipping sauce" style="left:186px;top:428px;width:60px;height:72px"></div>
  <div class="photo photo--seafood" role="img" aria-label="Photo of seafood platter" style="left:117px;top:490px;width:124px;height:78px"></div>
  <span class="photo-label" style="left:136px;top:453px">Empanada de<br>Cangrejo</span>
  <span class="photo-label" style="left:52px;top:523px">Palta Rellena<br>de Camarones</span>
  <span class="photo-label" style="left:72px;top:551px">Piqueo Marino</span>

  <div class="panel" style="left:270px;top:20px;width:224px;height:552px">
    <h2 class="section-title">Ensaladas / <small>Salads</small></h2>
    <div class="item"><div class="item-name">Ensalada de la Casa<span class="leader"></span>$6.95</div><p class="desc">lettuce, tomatoes, yellow peppers and zucchini</p></div>
    <div class="item"><div class="item-name">Ensalada Tamaru<span class="leader"></span>$7.95</div><p class="desc">lettuce, tomatoes, cucumbers, red onions, carrots, radish and avocado</p></div>
    <div class="item" style="margin-bottom:8px"><div class="item-name">Ensalada Cesar<span class="leader"></span>$8.95</div><p class="desc">romaine, lettuce, croutons, parmesan cheese and Tamaru's special sauce</p></div>
    <h2 class="section-title">Sopas / <small>Soups</small></h2>
    <div class="item"><div class="item-name">Aguadito Limeño</div><div class="variants"><span>Large<span class="leader"></span>$9.95</span><span>Small<span class="leader"></span>$5.95</span></div><p class="desc">chicken and vegetable soup mixed with rice and cilantro</p></div>
    <div class="item"><div class="item-name">Sopa a la Minuta<span class="leader"></span>$12.95</div><p class="desc">traditional milk and angel's hair pasta soup, served with beef and eggs</p></div>
    <div class="item"><div class="item-name">Caldo de Gallina<span class="leader"></span>$12.95</div><p class="desc">hen broth with noodles, scallion, potatoes and hard-boil egg</p></div>
    <div class="item"><div class="item-name">Chupe de Camarones Arequipeña<span class="leader"></span>$15.95</div><p class="desc">shrimp soup mixed with rice, green peas, Cusco corn, milk, eggs and Peruvian spices</p></div>
    <div class="item" style="margin-bottom:8px"><div class="item-name">Parihuela del Puerto<span class="leader"></span>$18.95</div><p class="desc">classic Peruvian seafood soup</p></div>
    <h2 class="section-title">Ceviche/ <small>Ceviches</small></h2>
    <div class="item"><div class="item-name">Leche de Tigre<span class="leader"></span>$10.95</div><p class="desc">ceviche marinade in fresh lime juice</p></div>
    <div class="item"><div class="item-name">Tiradito en Salsa de<br>Ají Amarillo<span class="leader"></span>$12.95</div><p class="desc">sashimi style fish in yellow pepper sauce and fresh lime juice, served with Cusco corn and sweet potatoes</p></div>
    <div class="item"><div class="item-name">Piqueo Chalaco<span class="leader"></span>$24.95</div><p class="desc">dish combined of Ceviche de Pescado (Fish Ceviche), and Jalea (Fried Seafood)</p></div>
    <div><div class="item-name">Ceviches <small style="font-size:7px">with-</small></div><div class="variants"><span>Pescado<span class="leader"></span>$15.95</span><span>Camaron<span class="leader"></span>$17.95</span></div><div class="variants"><span>Mixto<span class="leader"></span>$17.95</span></div><div class="variants"><span>Camaron con Pulpo<span class="leader"></span>$18.95</span></div><p class="desc">choice of raw fish, mixed seafood, shrimp or shrimp with octopus, marinated in fresh lime juice, served with red onions, Cusco corn and sweet potatoes</p></div>
  </div>

  <div class="cover">
    <div class="cover-menu">MENU</div>
    <div class="photo--scene" role="img" aria-label="Photo of mountain ruins in the Andes" style="left:8px;top:13px;width:246px;height:130px"></div>
    <div class="brand">Tamaru</div>
    <div class="cover-title" style="top:224px;font-size:30px;letter-spacing:1px">AUTHENTIC</div>
    <div class="cover-title" style="top:254px;font-size:15px;letter-spacing:1.5px">PERUVIAN CUISINE</div>
    <div class="cover-line" style="top:272px;font-size:13px;color:var(--gold)">217 Harbor Ave. New Rochelle, NY 10801</div>
    <div class="cover-line" style="top:292px;font-size:23px;font-weight:700">914-555-0172</div>
    <div class="cover-line" style="top:324px;font-size:13px">Delivery on order of $15 or more</div>
    <div class="cover-line" style="top:343px;font-size:11px">$5 fee for 3 miles or more</div>
    <div class="cover-line" style="top:365px;font-size:12.5px;line-height:1.35;color:var(--green-light)">Delivery Hours<br>Mon-Sun 11:30am - 10:00pm<br>Chef's Specials<br>on Weekends</div>
  </div>
  <div class="photo photo--seafood" role="img" aria-label="Photo of fish ceviche with corn and sweet potato" style="left:484px;top:445px;width:268px;height:110px"></div>
  <span class="photo-label" style="left:677px;top:546px">Ceviche Tamaru</span>
</section>

<section class="fold fold--inside">

  <div class="panel" style="left:19px;top:18px;width:224px;height:556px">
    <h2 class="section-title">Del Mar / <small>Seafood</small></h2>
    <div class="item"><div class="item-name">Pescado a lo Macho<span class="leader"></span>$19.95</div><p class="desc">fried fish fillet topped with seafood in hot yellow pepper sauce, served with rice and yuccas</p></div>
    <div class="item"><div class="item-name">Pescado Sudado<span class="leader"></span>$16.95</div><p class="desc">corvina fish stew, in hot yellow pepper, tomatoes, onions, served with rice and yuccas</p></div>
    <div class="item"><div class="item-name">Arroz con Mariscos<span class="leader"></span>$17.95</div><p class="desc">peruvian style paella, red rice served with seafood</p></div>
    <div class="item"><div class="item-name">Arroz Chaufa <small style="font-size:7px">with-</small></div><div class="variants"><span>Mariscos<span class="leader"></span>$17.95</span><span>Camarones<span class="leader"></span>$17.95</span></div><p class="desc">Peruvian style fried rice served with choice of seafood or shrimp</p></div>
    <div class="item"><div class="item-name">Trucha Frita<span class="leader"></span>$18.95</div><p class="desc">deep fried trout, served with white rice, fried yuccas and salsa criolla</p></div>
    <div><div class="item-name">Jalea</div><div class="variants"><span>Large<span class="leader"></span>$28.95</span><span>Small<span class="leader"></span>$17.95</span></div><p class="desc">deep fried mixed seafood and fish, served with fried yuccas</p></div>
    <div class="photo-slot" style="height:100px">
      <div class="photo photo--meat" role="img" aria-label="Photo of rotisserie chicken with rice and fries" style="left:-8px;top:6px;width:204px;height:82px"></div>
      <span class="photo-label" style="left:150px;top:88px">Pollo Tamaru</span>
    </div>
    <h2 class="section-title">Pollo a la Brasa / <small>Chicken</small></h2>
    <div class="item"><div class="item-name">1/4 Pollo<span class="leader"></span>$6.50</div><p class="desc">quarter chicken, served with two sides</p></div>
    <div class="item"><div class="item-name">1/2 Pollo<span class="leader"></span>$8.95</div><p class="desc">half chicken, served with two sides</p></div>
    <div class="item"><div class="item-name">1 Pollo<span class="leader"></span>$16.95</div><p class="desc">whole chicken, served with two sides</p></div>
    <div class="item"><div class="item-name">Pollo Limeño<span class="leader"></span>$20.95</div><p class="desc">whole chicken, served with French fries, avocado salad and yellow rice</p></div>
    <div class="item"><div class="item-name">Pollo Chalaco<span class="leader"></span>$26.95</div><p class="desc">whole chicken, served with avocado salad, salchipapa and yellow rice</p></div>
    <div><div class="item-name">Pollo Tamaru<span class="leader"></span>$30.95</div><p class="desc">whole chicken, served with avocado salad, arroz chaufa (chicken or steak) and salchipapa</p></div>
  </div>

  <div class="panel" style="left:270px;top:18px;width:224px;height:556px">
    <h2 class="section-title">Lo Mas Criollo<br><small>Traditional Dishes</small></h2>
    <div class="item" style="margin-bottom:5px"><div class="item-name">Parrillada Mixta<span class="leader"></span>$30.95</div><p class="desc">dish combined of grilled NY strip steak, anticuchos (Peruvian style kebabs), pork chops and sausage</p></div>
    <div class="item" style="margin-bottom:5px"><div class="item-name">Churrasco en Salsa de Camarones<span class="leader"></span>$20.95</div><p class="desc">NY strip steak topped with shrimps on hot yellow pepper sauce, served with rice</p></div>
    <div class="item" style="margin-bottom:5px"><div class="item-name">Seco Norteño<span class="leader"></span>$20.95</div><p class="desc">slowly cooked lamb stew in ají panka sauce, served with rice and Peruvian canario beans</p></div>
    <div class="item" style="margin-bottom:5px"><div class="item-name">Seco de Pato Piurano<span class="leader"></span>$17.95</div><p class="desc">slowly cooked duck stew in ají panka sauce, served with rice and hard-boiled yuccas</p></div>
    <div class="item" style="margin-bottom:5px"><div class="item-name">Tallarines Verdes con Churrasco<span class="leader"></span>$18.95</div><p class="desc">linguine pasta in Peruvian style pesto sauce served with grilled NY strip steak</p></div>
    <div class="item" style="margin-bottom:5px"><div class="item-name">Tacu Tacu <small style="font-size:7px">with-</small></div><div class="variants"><span>Churrasco<span class="leader"></span>$18.95</span><span>Lomo<span class="leader"></span>$15.95</span></div><p class="desc">Peruvian canario beans mixed with rice, served with choice of NY strip steak or wok-seared beef in soy sauce</p></div>
    <div class="item" style="margin-bottom:5px"><div class="item-name">Churrasco a lo Pobre<span class="leader"></span>$19.95</div><p class="desc">NY strip steak served with fried egg, sweet plantains, French fries and rice</p></div>
    <div class="item" style="margin-bottom:5px"><div class="item-name">Saltado <small style="font-size:7px">with-</small></div><div class="variants"><span>Lomo<span class="leader"></span>$15.95</span><span>Pollo<span class="leader"></span>$13.95</span></div><p class="desc">choice of wok-seared steak or chicken, mixed with red onions, tomatoes, in soy sauce, served with French fries and rice</p></div>
    <div class="item" style="margin-bottom:5px"><div class="item-name">Aeropuerto<span class="leader"></span>$18.95</div><p class="desc">Peruvian style fried rice, mixed with noodles, chicken, beef and shrimp</p></div>
    <div class="item" style="margin-bottom:5px"><div class="item-name">Arroz Chaufa <small style="font-size:7px">with-</small></div><div class="variants"><span>Carne<span class="leader"></span>$14.95</span><span>Pollo<span class="leader"></span>$12.95</span></div><p class="desc">Peruvian style fried rice mixed with choice of beef or chicken</p></div>
    <div class="item" style="margin-bottom:5px"><div class="item-name">Seco de Carne<span class="leader"></span>$15.95</div><p class="desc">beef ribs stew in ají panka sauce, served with rice and Peruvian canario beans</p></div>
    <div><div class="item-name">Ají de Gallina<span class="leader"></span>$11.95</div><p class="desc">shredded chicken in a spicy ají amarillo creamy sauce, hard-boiled egg, olives, potatoes and rice</p></div>
  </div>

  <div class="panel" style="left:523px;top:18px;width:234px;height:556px;padding-top:158px">
    <h2 class="section-title">Para Acompañar / <small>Sides</small></h2>
    <div class="item"><div class="item-name">Papas Fritas<span class="leader"></span>$3.95</div><p class="desc">French fries</p></div>
    <div class="item"><div class="item-name">Arroz Blanco o Amarillo<span class="leader"></span>$3.95</div><p class="desc">white / yellow rice</p></div>
    <div class="item"><div class="item-name">Frejoles<span class="leader"></span>$3.95</div><p class="desc">Peruvian canario beans</p></div>
    <div class="item"><div class="item-name">Maduros<span class="leader"></span>$3.95</div><p class="desc">sweet plantains</p></div>
    <div class="item"><div class="item-name">Tostones<span class="leader"></span>$3.95</div><p class="desc">fried green plantains</p></div>
    <div><div class="item-name">Yuca Frita<span class="leader"></span>$3.95</div><p class="desc">fried yuccas</p></div>
    <div class="photo-slot" style="height:92px">
      <span class="photo-label" style="left:0;top:4px">Picarones</span>
      <div class="photo" role="img" aria-label="Photo of picarones doughnuts" style="left:-2px;top:13px;width:118px;height:76px"></div>
      <div class="photo photo--meat" role="img" aria-label="Photo of lomo saltado" style="left:102px;top:2px;width:100px;height:76px"></div>
      <span class="photo-label" style="left:180px;top:72px;text-align:center">Lomo<br>Saltado</span>
    </div>
    <h2 class="section-title">Postres / <small>Dessert</small></h2>
    <div class="item"><div class="item-name">Crema Volteada<span class="leader"></span>$5.95</div><p class="desc">Peruvian caramel custard</p></div>
    <div class="item"><div class="item-name">Tres Leches<span class="leader"></span>$5.95</div><p class="desc">butter cake soaked in three kinds of milk</p></div>
    <div class="item"><div class="item-name">Torta Helada<span class="leader"></span>$5.95</div><p class="desc">sponge cake topped with strawberry jello</p></div>
    <div class="item"><div class="item-name">Torta de Chocholate<span class="leader"></span>$5.95</div><p class="desc">chocolate cake</p></div>
    <div><div class="item-name">Picarones<span class="leader"></span>$5.95</div><p class="desc">Peruvian style sweet potato doughnut covered with syrup</p></div>
  </div>
  <div class="photo" role="img" aria-label="Photo of tiradito with shrimp in yellow pepper sauce" style="left:476px;top:4px;width:138px;height:80px;background:radial-gradient(circle,#f7e9b8 0 40%,#e8c45a 70%,#d6d2c6 100%)"></div>
  <span class="photo-label" style="left:614px;top:30px">Tiradito con Camarones<br>en Ají Amarillo</span>
  <div class="photo photo--meat" role="img" aria-label="Photo of assorted traditional dishes" style="left:605px;top:53px;width:152px;height:113px"></div>
  <span class="photo-label" style="left:538px;top:118px">Puro Criollo</span>
</section>

</div>
</body>
</html>
```